Quillbrook IT company focused on 3 areas of IT

Looking for something similar to attached cards. Logo for quillbrook also attached.. Looking for something clean as far as colors (surprise me).. 3 tech stands for 3 primary areas, web design, consulting and network infrastructure design. Please email me if you have any questions. Looking forward to seeing how creative and professional this card will look. Thank you,

Target Market(s)

Small business/consumers looking for It services

Industry/Entity Type

It Service

Contact Information for Business Card

Darvin Pell
Principal Consultant

202-555-0173

www.quillbrook-example.com
dpell@quillbrook-example.com

46210 Marsh Lantern Ct,
Germantown, MD 20899

Colors

Designer to choose colors to be used in the design.

Requirements
Must have
• attached Logo design. Feel free to play with the colors.. If you have a better idea for a card, please fee free to send me. Looking for something clean/modern. Should have tech feel, not cheesy.
Nice to have
• Surprise me :-)..

```html
<!DOCTYPE html>
<html lang="en">
<head>
<meta charset="utf-8">
<title>Quillbrook – Business Card</title>
<link href="https://fonts.googleapis.com/css2?family=Work+Sans:wght@400;500;600&display=swap" rel="stylesheet">
<style>
  :root {
    --navy: #223a7a;
    --ink: #3a3a3a;
    --muted: #5c5c5c;
    --slate: #55565a;
    --paper: #ffffff;
    --stage: #e9eaed;
  }
  * { margin: 0; padding: 0; box-sizing: border-box; }
  html, body {
    width: 1200px; height: 930px; overflow: hidden;
    background: var(--stage);
    font-family: "Work Sans", Arial, sans-serif;
  }
  .canvas { position: relative; width: 1200px; height: 930px; }
  .card {
    position: absolute; width: 560px; height: 320px;
    box-shadow: 0 6px 18px rgba(0,0,0,0.18);
    overflow: hidden;
  }
  /* back side */
  .card-back { left: 120px; top: 110px; background: var(--navy); }
  .card-back .brand {
    position: absolute; left: 0; right: 0; top: 50%;
    transform: translateY(-50%);
    display: flex; align-items: center; justify-content: center; gap: 14px;
    color: var(--paper); font-weight: 600; font-size: 40px; letter-spacing: 1px;
  }
  .brand-square { width: 22px; height: 22px; border: 3px solid currentColor; }
  /* front side */
  .card-front { left: 520px; top: 500px; background: var(--paper); }
  .card-front .brand {
    position: absolute; left: 40px; top: 70px;
    display: flex; align-items: center; gap: 10px;
    color: var(--navy); font-weight: 600; font-size: 30px; letter-spacing: 0.5px;
  }
  .card-front .brand-square { width: 18px; height: 18px; }
  .holder {
    position: absolute; right: 42px; top: 128px; text-align: left;
  }
  .holder-name {
    color: var(--navy); font-weight: 500; font-size: 27px;
    text-transform: uppercase; letter-spacing: 0.5px; line-height: 1;
  }
  .holder-title { color: var(--muted); font-size: 13px; margin-top: 4px; letter-spacing: 0.3px; }
  .divider {
    position: absolute; left: 40px; right: 40px; top: 190px;
    height: 1px; background: var(--navy);
  }
  .contacts {
    position: absolute; left: 46px; top: 204px; list-style: none;
    font-size: 14px; color: var(--ink); line-height: 20px;
  }
  .contacts li { display: flex; align-items: center; gap: 8px; }
  .contacts svg { width: 11px; height: 11px; flex: none; }
  .contacts .web-domain { color: var(--navy); }
  .address {
    position: absolute; right: 42px; top: 212px;
    font-size: 14px; color: var(--ink); line-height: 20px; font-style: normal;
  }
  .bands { position: absolute; left: 0; bottom: 0; width: 560px; height: 22px; }
</style>
</head>
<body>
<main class="canvas">

  <section class="card card-back" aria-label="Card back">
    <div class="brand"><span class="brand-square"></span>Quillbrook</div>
  </section>

  <section class="card card-front" aria-label="Card front">
    <div class="brand"><span class="brand-square"></span>Quillbrook</div>

    <div class="holder">
      <p class="holder-name">Darvin Pell</p>
      <p class="holder-title">Principal Consultant</p>
    </div>

    <div class="divider"></div>

    <ul class="contacts">
      <li>
        <svg viewBox="0 0 12 12" aria-hidden="true"><path d="M2.5 1 L4.5 1 L5.2 3.4 L4 4.4 Q5 6.8 7.6 8 L8.6 6.8 L11 7.5 L11 9.5 Q10.5 11 9 11 Q1 10 1 2.6 Q1 1 2.5 1 Z" fill="var(--navy)"/></svg>
        202-555-0173
      </li>
      <li>
        <svg viewBox="0 0 12 12" aria-hidden="true"><rect x="1" y="2.5" width="10" height="7" fill="none" stroke="var(--navy)" stroke-width="1.2"/><path d="M1 2.5 L6 6.5 L11 2.5" fill="none" stroke="var(--navy)" stroke-width="1.2"/></svg>
        dpell@quillbrook-example.com
      </li>
      <li>
        <svg viewBox="0 0 12 12" aria-hidden="true"><circle cx="6" cy="6" r="5" fill="none" stroke="var(--navy)" stroke-width="1.1"/><ellipse cx="6" cy="6" rx="2.2" ry="5" fill="none" stroke="var(--navy)" stroke-width="1"/><path d="M1 6 H11" stroke="var(--navy)" stroke-width="1"/></svg>
        <span>www.<span class="web-domain">quillbrook-example</span>.com</span>
      </li>
    </ul>

    <address class="address">
      46210 Marsh Lantern Ct,<br>
      Germantown, MD 20899
    </address>

    <svg class="bands" viewBox="0 0 560 22" aria-hidden="true">
      <polygon points="0,12 344,12 340,22 0,22" fill="var(--navy)"/>
      <polygon points="350,4 560,4 560,22 344,22" fill="var(--slate)"/>
    </svg>
  </section>

</main>
</body>
</html>
```